" O nome Valtessora significa dentro do movimento. A clínica tem como carro chefe um trabalho chamado de videoanálise de movimento. Usamos um software para realizar análise de marcha, corrida, salto, estabilidade, flexibilidade entre outros. Identificamos alteraçoes no movimento que possam ser a causa de dor ou diminmuiçao no rendimento físico-funcional. Alteraçoes identificadas entramos com a reabilitaçao usando Pilates, RPG, Hidroterapia, Treinamento Funcional, Osteopatia entre outros. Nosso foco: resultados! "

```html
<!DOCTYPE html>
<html lang="pt-BR">
<head>
<meta charset="utf-8">
<title>Valtessora – Papel Timbrado</title>
<link rel="stylesheet" href="https://fonts.googleapis.com/css2?family=Archivo+Narrow:wght@400;700&family=Open+Sans:wght@400&display=swap">
<style>
  :root {
    --backdrop: #e6e6e6;
    --paper: #ffffff;
    --brand-blue: #1f3d8c;
    --brand-grey: #7d8796;
    --mark-faint: #e2e2e2;
    --footer-text: #4a4a4a;
  }
  html, body {
    margin: 0;
    padding: 0;
    width: 1200px;
    height: 1200px;
    overflow: hidden;
    background: var(--backdrop);
  }
  .letterhead {
    position: absolute;
    left: 210px;
    top: 48px;
    width: 780px;
    height: 1104px;
    background: var(--paper);
    overflow: hidden;
  }
  .brand {
    position: absolute;
    top: 66px;
    left: 0;
    right: 0;
    text-align: center;
  }
  .brand-dot {
    display: block;
    width: 34px;
    height: 34px;
    margin: 0 auto 8px;
    border-radius: 50%;
    background: var(--brand-blue);
  }
  .brand-name {
    margin: 0;
    font-family: "Archivo Narrow", sans-serif;
    font-weight: 700;
    font-size: 38px;
    line-height: 1;
    color: var(--brand-blue);
  }
  .brand-tagline {
    margin: 5px 0 0;
    font-family: "Archivo Narrow", sans-serif;
    font-weight: 400;
    font-size: 12px;
    letter-spacing: 0.3px;
    color: var(--brand-grey);
  }
  .watermark {
    position: absolute;
    left: 0;
    right: 0;
    top: 440px;
    margin: 0;
    text-align: center;
    font-family: "Archivo Narrow", sans-serif;
    font-weight: 700;
    font-size: 150px;
    line-height: 1;
    color: var(--mark-faint);
  }
  .contact {
    position: absolute;
    left: 0;
    right: 0;
    top: 1010px;
    text-align: center;
    font-family: "Open Sans", sans-serif;
    font-size: 15px;
    line-height: 20px;
    color: var(--footer-text);
  }
  .contact p { margin: 0; }
</style>
</head>
<body>
  <main class="letterhead">
    <header class="brand">
      <span class="brand-dot"></span>
      <h1 class="brand-name">Valtessora</h1>
      <p class="brand-tagline">Clínica de Análise do Movimento</p>
    </header>

    <p class="watermark" aria-hidden="true">Valtessora</p>

    <footer class="contact">
      <p>Endereço nono, 999 Cep: 99999-99 - Nonono- NO Fone: (99) 9999-9999</p>
      <p>contato@valtessora.com.br &nbsp;site: www.valtessora.com.br</p>
    </footer>
  </main>
</body>
</html>
```